Hair salon and Nail salon in Hawaii need a newspaper Ad design.

We need a newspaper Ad design for new open hair & nail salon in Waikiki Hawaii.Our Recommendation service for hair is "Head Spa" $30+tax and for nail is "Manicure Treatment Course" (Filing+Cuticle Care+Massage+Coloring) $20+tax.
We would like to see Hawaiian taste color and also having sense of luxury design. The ad size is W 5.0” x H 6.375”.
I would customers to know the shop place(Palisade Crestway Hotel 1F) , phone(808-555-0172), instagram(salonvelmara) , our web site https://salonvelmara.example and recommend services. For Web or Instagram , QR code is acceptable.

Target Market(s)

women & men

Industry/Entity Type

Beauty Salon

Font styles to use
Serif

Colors

Designer to choose colors to be used in the design.

Requirements
Must have
• Tagline for local customers. Shop Name is "SALON VELMARA".the shop place(Palisade Crestway Hotel 1F) , phone(808-555-0172), instagram(salonvelmara) and recommend services.
Nice to have
• Our services are competitive, but we don't want to be seen as just cheap and low quality.

```html
<!DOCTYPE html>
<html lang="en">
<head>
<meta charset="utf-8">
<title>Salon Velmara – Now Opening</title>
<link rel="stylesheet" href="https://fonts.googleapis.com/css2?family=Great+Vibes&family=Marcellus&family=Playfair+Display:wght@400;700;900&display=swap">
<style>
  :root {
    --peach: #f9b98a;
    --peach-light: #fbc398;
    --ink: #231f20;
    --pink: #e5519f;
    --badge: #ec4fa0;
    --purple: #8b5a9f;
    --white: #ffffff;
  }
  html, body { margin: 0; padding: 0; overflow: hidden; background: var(--white); }
  .ad {
    position: relative; width: 1200px; height: 988px; overflow: hidden;
    background: var(--peach); color: var(--ink);
    font-family: "Playfair Display", Georgia, serif;
  }
  .ad-shapes { position: absolute; inset: 0; }
  .abs { position: absolute; margin: 0; line-height: 1; white-space: nowrap; }

  .brand { left: 69px; top: 75px; display: flex; align-items: center; gap: 20px; }
  .brand-square { width: 78px; height: 81px; background: var(--ink); flex: none; }
  .brand-name { font-family: "Marcellus", Georgia, serif; font-size: 52px; letter-spacing: 2px; color: var(--ink); }

  .opening { left: 66px; top: 206px; font-family: "Great Vibes", cursive; font-size: 76px; color: var(--pink); }
  .headline { left: 66px; top: 282px; font-weight: 900; font-size: 96px; line-height: 0.92; letter-spacing: -1px; }
  .tagline { left: 74px; top: 499px; font-size: 24.5px; font-weight: 400; }

  .service-photo {
    position: absolute; border-radius: 50%; border: 4px solid var(--white);
    width: 140px; height: 140px;
  }
  .photo-spa { left: 57px; top: 549px; background: radial-gradient(circle at 45% 45%, #d9a98c, #6b3f2a); }
  .photo-nail { left: 321px; top: 549px; background: radial-gradient(circle at 40% 35%, #f1d2c2, #5a3526); }
  .price {
    position: absolute; width: 58px; height: 58px; border-radius: 50%;
    background: var(--badge); color: var(--white); text-align: center;
    font-weight: 700; font-size: 24px; line-height: 1;
  }
  .price .amt { display: block; padding-top: 10px; }
  .price .amt sup { font-size: 11px; vertical-align: 9px; }
  .price .tax { display: block; font-size: 9px; font-weight: 400; margin-top: 1px; }
  .price-spa { left: 151px; top: 653px; }
  .price-nail { left: 415px; top: 653px; }

  .service-title { font-weight: 700; font-size: 30px; line-height: 1.05; }
  .title-spa { left: 218px; top: 587px; }
  .title-nail { left: 486px; top: 561px; }
  .service-detail { left: 487px; top: 638px; font-size: 17px; line-height: 1.3; }

  .contact { display: flex; align-items: center; gap: 9px; font-size: 22px; white-space: nowrap; }
  .contact-icon {
    width: 34px; height: 34px; border-radius: 50%; background: var(--purple);
    display: flex; align-items: center; justify-content: center; flex: none;
  }
  .contact-phone { left: 254px; top: 753px; }
  .contact-place { left: 254px; top: 816px; align-items: flex-start; }
  .contact-place .contact-lines { line-height: 1.25; margin-top: 5px; }
  .contact-links { left: 254px; top: 899px; display: flex; align-items: center; gap: 22px; }
</style>
</head>
<body>
<main class="ad">
  <svg class="ad-shapes" viewBox="0 0 1200 988" width="1200" height="988">
    <defs>
      <linearGradient id="portrait-tone" x1="0" y1="0" x2="1" y2="1">
        <stop offset="0" stop-color="#c2bdb6"/>
        <stop offset="0.5" stop-color="#a8755c"/>
        <stop offset="1" stop-color="#6e4330"/>
      </linearGradient>
      <linearGradient id="storefront-tone" x1="0" y1="0" x2="0" y2="1">
        <stop offset="0" stop-color="#d8d6d2"/>
        <stop offset="0.6" stop-color="#bdb7ae"/>
        <stop offset="1" stop-color="#3a3330"/>
      </linearGradient>
      <radialGradient id="foliage-tone" cx="0.2" cy="0.85" r="0.8">
        <stop offset="0" stop-color="#2f9a78"/>
        <stop offset="0.55" stop-color="#5cbf94" stop-opacity="0.85"/>
        <stop offset="1" stop-color="#f08d5a" stop-opacity="0"/>
      </radialGradient>
    </defs>

    <path class="backdrop-curve" d="M560 0 C 650 200 720 420 690 640 C 670 800 690 920 720 988 L 1200 988 L 1200 0 Z" fill="var(--peach-light)"/>

    <ellipse class="foliage" role="img" aria-label="Tropical leaves and hibiscus flowers" cx="90" cy="880" rx="300" ry="300" fill="url(#foliage-tone)"/>

    <path class="portrait-frame" d="M705 0 C 668 110 664 230 680 360 C 700 520 690 700 734 988 L 1200 988 L 1200 0 Z" fill="var(--white)"/>
    <path class="portrait-photo" role="img" aria-label="Model with long wavy hair and red manicured nails, framed by tropical leaves" d="M767 0 C 720 90 692 200 695 300 C 698 420 712 520 740 600 C 760 640 775 660 785 680 L 785 988 L 1200 988 L 1200 0 Z" fill="url(#portrait-tone)"/>

    <ellipse class="storefront-frame" cx="994" cy="838" rx="280" ry="292" fill="var(--white)"/>
    <ellipse class="storefront-photo" role="img" aria-label="Glass storefront of the salon with interior chairs and opening-hours sign" cx="994" cy="840" rx="268" ry="279" fill="url(#storefront-tone)"/>
  </svg>

  <div class="abs brand">
    <span class="brand-square" aria-hidden="true"></span>
    <span class="brand-name">SALON VELMARA</span>
  </div>

  <p class="abs opening">Now Opening</p>
  <h1 class="abs headline">HAIR &amp; NAIL<br>SALON</h1>
  <p class="abs tagline">Treat Yourself with Our Recommendation Service</p>

  <div class="service-photo photo-spa" role="img" aria-label="Woman relaxing during a head spa treatment"></div>
  <div class="price price-spa"><span class="amt"><sup>$</sup>30</span><span class="tax">+tax</span></div>
  <h2 class="abs service-title title-spa">Head<br>Spa</h2>

  <div class="service-photo photo-nail" role="img" aria-label="Hands receiving a manicure with dark polish"></div>
  <div class="price price-nail"><span class="amt"><sup>$</sup>20</span><span class="tax">+tax</span></div>
  <h2 class="abs service-title title-nail">Manicure<br>Treatment Course</h2>
  <p class="abs service-detail">Filing + Cuticle Care +<br>Massage + Coloring</p>

  <div class="abs contact contact-phone">
    <span class="contact-icon">
      <svg width="18" height="18" viewBox="0 0 24 24"><path fill="#fff" d="M6.6 10.8a15.1 15.1 0 0 0 6.6 6.6l2.2-2.2a1 1 0 0 1 1-.25 11.4 11.4 0 0 0 3.6.57 1 1 0 0 1 1 1V20a1 1 0 0 1-1 1A17 17 0 0 1 3 4a1 1 0 0 1 1-1h3.5a1 1 0 0 1 1 1c0 1.25.2 2.45.57 3.57a1 1 0 0 1-.25 1z"/></svg>
    </span>
    <span>808-555-0172</span>
  </div>

  <div class="abs contact contact-place">
    <span class="contact-icon">
      <svg width="16" height="18" viewBox="0 0 24 24"><path fill="#fff" d="M12 2a7 7 0 0 0-7 7c0 5.2 7 13 7 13s7-7.8 7-13a7 7 0 0 0-7-7zm0 9.5A2.5 2.5 0 1 1 12 6.5a2.5 2.5 0 0 1 0 5z"/></svg>
    </span>
    <span class="contact-lines">Palisade Crestway Hotel 1F<br>1280 Kalena Street, Honolulu, HI 96815</span>
  </div>

  <div class="abs contact-links">
    <div class="contact contact-web">
      <span class="contact-icon">
        <svg width="20" height="20" viewBox="0 0 24 24" fill="none" stroke="#fff" stroke-width="1.8"><circle cx="12" cy="12" r="9"/><path d="M3 12h18M12 3c3 3.2 3 14.8 0 18M12 3c-3 3.2-3 14.8 0 18"/></svg>
      </span>
      <span>salonvelmara.example</span>
    </div>
    <div class="contact contact-insta">
      <span class="contact-icon" aria-hidden="true"></span>
      <span>salonvelmara</span>
    </div>
  </div>
</main>
</body>
</html>
```